A private psychotherapy practice for seniors located on the upper west side of manhattan needs a pos

**Hi, Please note deadline was decreased by two days**

I am a Psychotherapist (LCSW) who has a Private Practice located on the Upper West Side of Manhattan. I accept Vitalcare and most other insurances. I treat Seniors who have health or financial issues, loss of spouse, feel sad most days, withdraw from social activities or have problems sleeping or eating. Psychotherapy allows individuals to relieve their feelings of sadness and to enjoy life again. I am a licensed clinical social worker with over fifteen years of experience and advanced training from Calderwood Analytic Academy.

Target Market(s)

Senior Citizens (65+) living on the upper west side of manhattan

Font styles to use
Serif

Requirements
Must have
• Broad appeal - diversified ethnic group if photos are used. Clear call to help those struggling with aging issues - especially living in New York City
Nice to have
• Hopeful and improved quality of life as result of psychotherapy treatment. Improved relations with family and friends.
Should not have
• Not depressing or too psycho bable.

```html
<!DOCTYPE html>
<html lang="en">
<head>
<meta charset="utf-8">
<title>Miriam Hale – Private Psychotherapist Postcard</title>
<link href="https://fonts.googleapis.com/css2?family=Open+Sans:ital,wght@0,400;0,600;0,700;1,400&display=swap" rel="stylesheet">
<style>
  :root{
    --teal:#2b8fae;
    --teal-dark:#1e6b8c;
    --badge:#235f86;
    --sky:#e3f2f8;
    --sky-mid:#bfe0ee;
    --ink:#4a4a4a;
    --ink-soft:#6b6b6b;
    --line:#c9c9c9;
    --paper:#ffffff;
    --backdrop:#e9e6e1;
  }
  *{box-sizing:border-box;margin:0;padding:0}
  html,body{width:878px;height:1200px;overflow:hidden}
  body{background:var(--backdrop);font-family:"Open Sans",Arial,sans-serif;color:var(--ink);position:relative}
  .card{position:absolute;left:39px;width:800px;height:540px;background:var(--paper);box-shadow:0 6px 18px rgba(0,0,0,.18);overflow:hidden}
  .card--front{top:40px}
  .card--back{top:620px}

  /* front */
  .front__headline{position:absolute;left:0;top:0;width:100%;height:92px;background:linear-gradient(180deg,#f2f9fc,var(--sky));display:flex;align-items:center;justify-content:center;text-align:center;color:var(--teal);font-weight:700;font-size:24px;line-height:1.3;padding:0 60px}
  .front__art{position:absolute;left:0;top:92px}
  .front__badge{position:absolute;left:622px;top:298px;width:142px;height:142px;border-radius:50%;background:var(--badge);border:5px solid var(--paper);box-shadow:0 0 0 2px var(--sky-mid);color:#fff;font-size:13px;line-height:1.35;text-align:center;display:flex;align-items:center;justify-content:center;padding:16px}
  .front__name{position:absolute;left:30px;top:438px;color:var(--teal);font-size:27px;font-weight:700}
  .front__role{position:absolute;left:30px;top:476px;color:var(--ink);font-size:17px;font-weight:600}
  .front__phone{position:absolute;left:600px;top:464px;display:flex;align-items:center;gap:10px;color:var(--ink);font-size:20px;font-weight:600}

  /* back */
  .back__art{position:absolute;left:0;top:0}
  .back__name{position:absolute;left:38px;top:186px;color:var(--teal);font-size:25px;font-weight:700}
  .back__role{position:absolute;left:38px;top:222px;font-size:16px;font-weight:600;color:var(--ink)}
  .back__body{position:absolute;left:38px;top:268px;width:360px;font-size:14.5px;line-height:1.55;color:var(--ink-soft)}
  .back__body p{margin-bottom:16px}
  .back__body .back__note{font-style:italic}
  .back__address{position:absolute;left:478px;top:26px;font-size:12px;line-height:1.45;color:var(--ink)}
  .back__stamp{position:absolute;left:684px;top:24px;width:88px;height:96px;border:1.5px solid var(--line)}
  .back__lines{position:absolute;left:520px;top:290px;width:250px}
  .back__lines span{display:block;height:1px;background:var(--line);margin-bottom:42px}
</style>
</head>
<body>

<section class="card card--front">
  <h1 class="front__headline">Psychotherapy allows individuals to relieve their feelings of sadness and to enjoy life again.</h1>

  <svg class="front__art" width="800" height="360" viewBox="0 0 800 360">
    <defs>
      <linearGradient id="photoTone" x1="0" y1="0" x2="1" y2="1">
        <stop offset="0" stop-color="#d9c7ae"/>
        <stop offset=".5" stop-color="#c7a98a"/>
        <stop offset="1" stop-color="#e8ddd0"/>
      </linearGradient>
    </defs>
    <path d="M0 0H800V250C620 300 420 230 230 260 130 276 50 300 0 300Z" fill="url(#photoTone)" role="img" aria-label="Photo of smiling senior friends of diverse backgrounds sharing a meal together"/>
    <path d="M0 300C60 292 140 270 240 262 420 244 600 300 800 252V272C610 320 420 262 240 282 140 292 60 310 0 318Z" fill="var(--sky-mid)"/>
    <path d="M0 318C80 306 170 292 260 288 440 280 620 318 800 276V286C620 332 440 294 260 302 170 306 80 320 0 330Z" fill="var(--sky)"/>
  </svg>

  <div class="front__badge">Private Practice located on the Upper West Side of Manhattan</div>

  <h2 class="front__name">Miriam Hale</h2>
  <p class="front__role">Private Psychotherapist (LCSW)</p>
  <p class="front__phone">
    <svg width="26" height="26" viewBox="0 0 24 24" aria-hidden="true"><circle cx="12" cy="12" r="12" fill="var(--teal)"/><path d="M8.2 6.5l2 2.3-1.1 1.5c.8 1.6 2 2.8 3.6 3.6l1.5-1.1 2.3 2-1 1.8c-4.1-.3-8.2-4.4-8.5-8.5z" fill="#fff"/></svg>
    000 000 000
  </p>
</section>

<section class="card card--back">
  <svg class="back__art" width="800" height="540" viewBox="0 0 800 540">
    <defs>
      <linearGradient id="handsTone" x1="0" y1="0" x2="1" y2="0">
        <stop offset="0" stop-color="#f3ede6"/>
        <stop offset=".5" stop-color="#c89b7c"/>
        <stop offset="1" stop-color="#efe7de"/>
      </linearGradient>
      <linearGradient id="panelTone" x1="0" y1="0" x2="0" y2="1">
        <stop offset="0" stop-color="#ffffff"/>
        <stop offset="1" stop-color="#eef7fb"/>
      </linearGradient>
    </defs>
    <rect x="0" y="0" width="440" height="540" fill="url(#panelTone)"/>
    <rect x="0" y="0" width="430" height="172" fill="url(#handsTone)" role="img" aria-label="Photo of a younger hand gently holding an older hand"/>
    <path d="M420 0C470 140 470 400 420 540H440C492 400 492 140 440 0Z" fill="var(--sky-mid)"/>
    <path d="M440 0C494 140 494 400 440 540H452C506 400 506 140 452 0Z" fill="var(--teal)" opacity=".55"/>
  </svg>

  <h2 class="back__name">Miriam Hale</h2>
  <p class="back__role">Private Psychotherapist (LCSW)</p>
  <div class="back__body">
    <p>I treat Seniors who have health or financial issues, loss of spouse, feel sad most days, withdraw from social activities or have problems sleeping or eating.</p>
    <p>Licensed clinical social worker with over 15 years of experience and advanced training from Calderwood Analytic Academy.</p>
    <p class="back__note">I accept Vitalcare and most other insurances.</p>
  </div>

  <address class="back__address" style="font-style:normal">
    Miriam Hale<br>
    415 Riverside Dr Apt 3B<br>
    New York, NY 10025-4102<br>
    Membership ID: 504217
  </address>
  <div class="back__stamp" aria-label="Stamp area"></div>
  <div class="back__lines" aria-hidden="true"><span></span><span></span><span></span><span></span></div>
</section>

</body>
</html>
```